Geschäftspapiere für Jobwebseite
Zielgruppe
Hier finden sie alle Informationen zu unserem Unternehmen:
https://www.blauer-kranich.com
Aufgabenstellung
Gerne von den Farben angelehnt an die Website ein modernes Briefpapier gestalten.

```html
<!DOCTYPE html>
<html lang="de">
<head>
<meta charset="utf-8">
<title>Briefpapier – Blauer-Kranich.de</title>
<link href="https://fonts.googleapis.com/css2?family=Noto+Sans:wght@400;700&display=swap" rel="stylesheet">
<style>
  :root {
    --backdrop: #393939;
    --paper: #f7f7f7;
    --ink: #2b2f3a;
    --text: #4a4a4a;
    --muted: #6e6e6e;
    --green: #00843d;
  }
  * { box-sizing: border-box; margin: 0; padding: 0; }
  html, body {
    width: 1200px; height: 860px; overflow: hidden;
    background: var(--backdrop);
    font-family: "Noto Sans", Verdana, sans-serif;
  }
  .letterhead {
    position: absolute; left: 310px; top: 20px;
    width: 580px; height: 820px;
    background: var(--paper);
    color: var(--text);
  }
  .brand {
    position: absolute; top: 120px; left: 0; width: 100%;
    display: flex; justify-content: center; align-items: center; gap: 6px;
  }
  .brand-name {
    font-weight: 700; font-size: 19px; color: var(--ink); letter-spacing: 0.2px;
  }
  .brand-dot {
    width: 10px; height: 10px; border-radius: 50%; background: var(--green);
  }
  .sender-line {
    position: absolute; top: 262px; left: 72px;
    font-size: 6.5px; color: var(--muted);
  }
  .sender-line strong { color: var(--green); font-weight: 700; }
  .recipient {
    position: absolute; top: 276px; left: 72px;
    font-size: 9.5px; line-height: 13px; color: var(--text);
  }
  .fold-mark {
    position: absolute; left: 18px; top: 290px;
    width: 8px; height: 1px; background: var(--green);
  }
  .letter-body {
    position: absolute; top: 372px; left: 72px; width: 400px;
    font-size: 8.6px; line-height: 12px; color: var(--text);
  }
  .letter-body p { margin-bottom: 12px; }
  .salutation { margin-bottom: 22px !important; }
  .legal-footer {
    position: absolute; right: 28px; top: 200px; height: 560px;
    writing-mode: vertical-rl; transform: rotate(180deg);
    font-size: 6px; line-height: 10px; color: var(--muted);
    text-transform: uppercase; letter-spacing: 0.2px;
  }
  .legal-footer strong { color: var(--ink); font-weight: 700; }
  .legal-footer .legal-brand { color: var(--green); }
  .footer-rule {
    position: absolute; right: 24px; top: 768px;
    width: 1px; height: 14px; background: var(--green);
  }
</style>
</head>
<body>
  <main class="letterhead">
    <header class="brand">
      <span class="brand-name">BLAUER-KRANICH.de</span>
      <span class="brand-dot"></span>
    </header>

    <p class="sender-line"><strong>BLAUER-KRANICH.DE</strong> | Kranichweg 4 | 76999 Talbach</p>
    <address class="recipient" style="font-style:normal">
      Firma: Musterfirma<br>
      Herr Maximilian Mustermann<br>
      Musterstraße 11<br>
      12345 Musterstadt
    </address>
    <span class="fold-mark"></span>

    <section class="letter-body">
      <p class="salutation">Sehr geehrter Herr Mustermann,</p>
      <p>Ferem sit, omniendaecte doluptature mo cuptatio. Ebitati ssumqui coria poreici destrum, vidusap elibus qui ipideli tatecabo. Et remporporio di quo ommolup taessit, ius non esequibus et volupiditio optatur ereicat laut et et quae ium int ma sum cori omnimin recus, ent molupti orrores truptassin eos a cor sa sus dolupta sitist laut que plignat. Axim exeribus. Pudit arum ium ipiet in ni od mos ent liciam quunt aborporem verferr uptasim ra de int quunt a inimin et il mi, eaque volo bla volo bea qui ius, sum volo ibus, acepernatem aut explabo rporupta pa qui consediam atus.</p>
      <p>Aximporporum et dolore conecerferia venimet verae sum nobist asintorest, eosant alique volut qui te nullo eum que velitatatis iumque mint ut volupta tquiatemodi dolless itature, et laccuptae pa invelis sequunt, velique abo. Obis sus et officipsamus premquidi blabo. Dollore matend untiatu reperion consequam faccaborit faciates sitatenet harunt invenim di sumque.</p>
      <p>Pore oditam identiitlis dit estrunt officta tecust pro maionsequis del mos aut quiatur? Icillab ipsapie nihilluptas mo et que sitatis dolupta quament laborro cuptae. Namus, utendunt.Pictat. Otae nimet faccatur? Erumqui at occum ratquia nos viti con reiunt volorro omnodit, nusam ratiasr itatet pa quistionsed explitem. Nam inis essinve litatib usdandit miliasinces utatem facia volesci allt evel iuntis unt ab illit autem quam archilluptae.</p>
      <p>Ihicium rerum as reperae porempedi neces et acculparum fugiae denetur, torerrovit ullenis arum re dolessi sum rerum ra di que vel minciam duntio. Aborios ent quiaerci sus andigente sincius si occum fugiae reperibus delicab is blandiscia quo dolorro vitasped evelest, suntemp oreictor a porentam si quae volorro rerferia volorepeliti ad ma voluptat acest offictis aperor maio. Ut liquam erum eum dunt offici que pla sitis exped maio. Nam sitatur sit qui comculparc hilite nonsequia autemquat.</p>
    </section>

    <aside class="legal-footer">
      <div><strong>Geschäftsführer</strong> Herr Jonas Wendler | <strong>Amtsgericht</strong> Talbach | <strong>Telefon</strong> +49 (0)7000 123 456 7 | <strong>Mail</strong> info@blauer-kranich.de | <strong>Web</strong> www.blauer-kranich.de</div>
      <div><strong class="legal-brand">Blauer-Kranich.de</strong> | Kranichweg 4 | 76999 Talbach | HRB XXXX | USt-IdNr. DEXXXXXXXXX | www.blauer-kranich.com</div>
    </aside>
    <span class="footer-rule"></span>
  </main>
</body>
</html>
```